Group Medical Practice needs stationery, business cards etc. designed

We need stationery designed for a multisite practice that offers primary medical, dental and behavioral healthcare. We would like a design that is consistent for letterhead, business cards, Microsoft Outlook stationery etc. We have attached our new logo design.

Business

```html
<!DOCTYPE html>
<html lang="en">
<head>
<meta charset="utf-8">
<title>Ridgeview Care Group – Stationery</title>
<link href="https://fonts.googleapis.com/css2?family=Fira+Sans:wght@400;500&display=swap" rel="stylesheet">
<style>
  :root {
    --backdrop: #e6e6e6;
    --paper: #ffffff;
    --brand-green: #8cc63f;
    --brand-blue: #1b75bc;
    --text-grey: #555555;
    --text-soft: #6a6a6a;
    --edge: #cfcfcf;
  }
  * { margin: 0; padding: 0; box-sizing: border-box; }
  html, body { width: 1000px; height: 1200px; overflow: hidden; }
  body {
    position: relative;
    background: var(--backdrop);
    font-family: "Fira Sans", sans-serif;
    color: var(--text-grey);
  }
  .sheet {
    position: absolute;
    background: var(--paper);
    border: 1px solid var(--edge);
    overflow: hidden;
  }
  .wordmark {
    position: absolute;
    color: var(--brand-blue);
    font-weight: 500;
    white-space: nowrap;
    display: flex;
    align-items: center;
    gap: 8px;
  }
  .wordmark .dot {
    display: inline-block;
    border-radius: 50%;
    background: var(--brand-green);
  }
  .rule-h, .rule-v { position: absolute; background: var(--brand-green); }

  /* Business card front */
  .card-front { left: 147px; top: 47px; width: 276px; height: 153px; }
  .card-front .wordmark { left: 0; right: 0; top: 62px; justify-content: center; font-size: 19px; }
  .card-front .wordmark .dot { width: 14px; height: 14px; }

  /* Business card back */
  .card-back { left: 490px; top: 47px; width: 276px; height: 153px; }
  .card-back .wordmark { left: 17px; top: 36px; font-size: 12px; gap: 6px; }
  .card-back .wordmark .dot { width: 9px; height: 9px; }
  .card-back .rule-h { left: 0; right: 0; top: 69px; height: 2px; }
  .card-back .rule-v { left: 133px; top: 123px; width: 2px; height: 30px; }
  .card-back .person { position: absolute; right: 25px; top: 85px; text-align: right; }
  .card-back .person-name { color: var(--brand-blue); font-size: 15px; font-weight: 500; line-height: 18px; }
  .card-back .person-role { font-size: 9px; color: var(--text-soft); line-height: 12px; }
  .card-back .address { position: absolute; right: 152px; top: 124px; text-align: right; font-size: 7px; line-height: 10px; color: var(--text-soft); }

  /* Letterhead */
  .letterhead { left: 180px; top: 237px; width: 644px; height: 910px; }
  .letterhead .wordmark { left: 42px; top: 62px; font-size: 22px; gap: 10px; }
  .letterhead .wordmark .dot { width: 16px; height: 16px; }
  .letterhead .rule-v { left: 443px; top: 0; width: 2px; height: 125px; }
  .letterhead .rule-h { left: 0; right: 0; top: 124px; height: 3px; }
  .letterhead .contact { position: absolute; left: 455px; top: 36px; font-size: 10px; line-height: 12px; color: var(--text-soft); letter-spacing: 0.2px; }
  .letterhead .contact b { font-weight: 500; color: var(--text-grey); }
  .letter-body { position: absolute; left: 111px; top: 196px; width: 480px; font-size: 12.3px; line-height: 15.9px; color: var(--text-grey); }
  .letter-body p { margin-bottom: 15.9px; }
  .signature { position: absolute; right: 67px; top: 668px; text-align: right; }
  .signature .person-name { color: var(--brand-blue); font-size: 17px; font-weight: 400; line-height: 20px; }
  .signature .person-role { font-size: 12px; color: var(--text-soft); line-height: 16px; }
  .letterhead .footer-mark { left: 0; right: 0; top: 800px; justify-content: center; color: var(--brand-green); font-size: 44px; gap: 14px; }
  .letterhead .footer-mark .dot { width: 30px; height: 30px; }
</style>
</head>
<body>

  <section class="sheet card-front">
    <div class="wordmark"><span class="dot"></span>Ridgeview Care Group</div>
  </section>

  <section class="sheet card-back">
    <div class="wordmark"><span class="dot"></span>Ridgeview Care Group</div>
    <div class="rule-h"></div>
    <div class="person">
      <div class="person-name">Daniel Hartley</div>
      <div class="person-role">President and C.E.O</div>
    </div>
    <div class="address">42 Cedar Lane Ste 210<br>Brookfield, Ohio 44403</div>
    <div class="rule-v"></div>
  </section>

  <section class="sheet letterhead">
    <div class="wordmark"><span class="dot"></span>Ridgeview Care Group</div>
    <div class="rule-v"></div>
    <div class="contact">
      42 Cedar Lane Ste 210<br>
      Brookfield, Ohio 44403<br>
      <b>Phone</b>&nbsp; 00987 654 321<br>
      <b>Fax</b>&nbsp;&nbsp; 00 987 654 32
    </div>
    <div class="rule-h"></div>

    <div class="letter-body">
      <p>Lorem ipsum dolor sit amet,</p>
      <p>Consectetur adipiscing elit. Mauris at vestibulum elit. Mauris sed malesuada<br>
      turpis, nec lobortis mi. Proin nec lacus condimentum, mattis dolor nec, luctus<br>
      enim. Nunc in nunc metus. Donec convallis diam mauris, quis eleifend odio<br>
      tincidunt sed. Proin sed nulla aliquet, tincidunt est sit amet, eleifend ipsum.<br>
      Aenean vitae maximus metus, at hendrerit enim. Donec cursus ante sed<br>
      euismod tempus. Nam quis tortor varius, pellentesque tortor ac, porta mi.<br>
      Integer lorem sem, mollis ac pulvinar ac, rutrum vitae massa. Nam ut mauris<br>
      id tellus aliquam commodo. Proin iaculis turpis ut arcu ullamcorper, vel<br>
      commodo mauris feugiat. Etiam finibus in nisl sit amet ultrices.</p>
      <p>Pellentesque non efficitur nibh. In sollicitudin accumsan velit. Cras mollis<br>
      erat lectus, et ultrices felis vehicula sed. Proin odio libero, consectetur non<br>
      felis quis, scelerisque fringilla urna. Cras venenatis rhoncus enim, id finibus<br>
      nibh maximus ut. Morbi scelerisque laoreet tempor. Phasellus dignissim<br>
      lectus at lacus interdum pulvinar. Ut pulvinar imperdiet massa, ac molestie<br>
      magna cursus non. Duis diam erat, finibus ac venenatis nec, gravida vel arcu.<br>
      Pellentesque non rutrum nibh. Aenean tristique metus et libero ornare pre-<br>
      tium. Nullam fermentum mollis vulputate.</p>
      <p>Vestibulum a pulvinar ante, auctor porttitor sapien. Fusce ornare, dolor<br>
      posuere viverra scelerisque, lacus dui efficitur ante, non lacinia ligula ligula<br>
      lacinia velit. Suspendisse finibus nulla ac vulputate tincidunt</p>
    </div>

    <div class="signature">
      <div class="person-name">Daniel Hartley</div>
      <div class="person-role">President and C.E.O</div>
    </div>

    <div class="wordmark footer-mark"><span class="dot"></span>Ridgeview Care Group</div>
  </section>

</body>
</html>
```